ECommerce Site Redesign: overall site and specific pages

We have a website that has been in operation for 6+ years, and it's time for a visual refresh.

Our current website is located at http://trk.example

The only significant functional change will be the movement of the persistent vertical navigation bar from the left side up to a categorized horizontal navigation menu. I've attached a rough mockup of how we want this positioned.

No coding necessary; just PSDs. The attached ROUGH MENU MOCKUP.PSD contains a layer with our logo on white should you wish to include it in your submissions.

Target Market(s)

We are an outdoor retailer focused on the high end of the market. We have a general color scheme on our site which we'd like to keep, but various elements need to be made consistent and more aesthetically pleasing.

Our brand is very important to us, and the site design must reflect our values of high quality and affluence. We cater to outdoor enthusiasts, hikers, back packers, and general high end apparel consumers.

Requirements
Must have
• In order to address the issue of consistency, we require strict design guidelines, including font sizing, element spacing, etc.

We require 7 page design templates for:

1.) overall site template - see http://trk.example for current.
* narrow static header bar (NEW)
* footer (KEEP SAME/SIMILAR)
* background
* body
* mini-cart (collapsed and expanded)
* promotion panel (ad box, rotating featured items)
* horizontal navigation bars (expanded/collapsed, grouped by 7 main categories) - see attached ROUGH MENU MOCKUP and see additional notes.
* recently viewed products

2.) product page (see http://trk.example/270599/frostline_summit-cowl-merino-mens.aspx for current)
* product imagery/zoombox
* color, size, quantity selection
* add to cart button
* detail tabs
* In-store Availability info
* info panel near the add to cart box for exceptions including:
- Available to pick up in-store only
- Free shipping for your entire order when you purchase this item
- This item is over-sized; please contact a store directly
* "customers who bought this also bought" panel, grid listing of items

3.) product listings (category, search results, etc.)
* item thumbnails in grid format
* sidebar for refinement options (by supplier, by price, by size, etc.)

4.) generic information/content page (see http://trk.example/t-returns.aspx)

5.) store locations page (see http://trk.example/t-TRK.stores.04.aspx)
* store details
* map
* hours
* contact info
* local links
* contact form

6.) contact us form

7.) checkout (see attached current checkout screen shot)
* cart summary
* checkout steps

Any visual elements benefiting from hover effects will need to have both dimmed and hovered layers in the design.

```html
<!DOCTYPE html>
<html lang="en">
<head>
<meta charset="utf-8">
<title>Timberkeel Outfitters – Backpacks</title>
<link rel="stylesheet" href="https://fonts.googleapis.com/css2?family=Ubuntu:wght@400;500;700&display=swap">
<style>
:root{
  --topbar-light:#4f93ea;
  --topbar-dark:#1d5fc4;
  --white:#ffffff;
  --page-shadow:rgba(60,40,100,.18);
  --brand:#6a4aa8;
  --nav-top:#a88bd0;
  --nav-bottom:#8a68c0;
  --nav-active:#b9a0dc;
  --stage-top:#8c6bc0;
  --stage-bottom:#d9cbeb;
  --side-item:#b49bd8;
  --side-line:#c7b4e3;
  --side-active:#ece5f6;
  --panel:#e9e1f4;
  --heading:#5b3a98;
  --body-text:#9b84c8;
  --card-label:#b09ad6;
  --card-price:#8fa0d8;
  --search-bg:#eeeeee;
  --search-border:#d4d4d4;
  --search-text:#a8a8a8;
  --logo-ink:#3d3d3d;
}
*{box-sizing:border-box;margin:0;padding:0}
html,body{width:1200px;height:1045px;overflow:hidden;background:var(--white);font-family:"Ubuntu",sans-serif}
.canvas{position:relative;width:1200px;height:1045px;overflow:hidden}

.topbar{position:absolute;left:0;top:0;width:1200px;height:38px;
  background:linear-gradient(var(--topbar-light),var(--topbar-dark));color:var(--white);font-size:15px}
.topbar-links{position:absolute;left:106px;top:0;height:38px;display:flex;align-items:center;list-style:none}
.topbar-links li{padding:0 14px;border-left:1px solid rgba(255,255,255,.35);line-height:22px}
.topbar-links li:first-child{padding-left:12px;border-left:none}
.cart-summary{position:absolute;right:94px;top:5px;display:flex;align-items:center;gap:8px;font-size:13.5px}
.checkout-btn{background:linear-gradient(#a9c9f4,#7fa9e6);color:var(--white);border-radius:4px;padding:6px 9px;font-size:13.5px}

.page{position:absolute;left:94px;top:38px;width:1012px;height:1007px;background:var(--white);box-shadow:0 0 18px var(--page-shadow)}

.logo{position:absolute;left:118px;top:52px;color:var(--brand);font-weight:700;line-height:1}
.logo-name{font-size:46px;letter-spacing:2px}
.logo-sub{font-size:15px;letter-spacing:21px;margin-top:4px;padding-left:80px}

.search{position:absolute;left:795px;top:66px;width:214px;height:31px;background:var(--search-bg);
  border:1px solid var(--search-border);border-radius:4px;color:var(--search-text);font-size:15px;line-height:29px;padding-left:8px}
.search-btn{position:absolute;left:1020px;top:66px;width:32px;height:32px}

.stage{position:absolute;left:106px;top:132px;width:988px;height:913px;
  background:linear-gradient(var(--stage-top) 0,var(--stage-bottom) 300px,var(--side-line) 100%)}
.mainnav{position:absolute;left:0;top:0;width:988px;height:39px;display:flex;list-style:none;
  background:linear-gradient(var(--nav-top),var(--nav-bottom))}
.mainnav li{width:123.5px;text-align:center;line-height:39px;color:var(--white);font-size:16px;border-left:1px solid rgba(255,255,255,.18)}
.mainnav li:first-child{border-left:none}
.mainnav .is-active{background:var(--nav-active);font-weight:700}

.hero{position:absolute;left:10px;top:52px;width:965px;height:257px;box-shadow:0 2px 8px rgba(50,20,90,.35);
  background:linear-gradient(#6f95c8 0%,#a9c7e8 55%,#c4d7ec 70%,#7e9fc6 78%,#9fbbdc 100%)}
.hero-credit{position:absolute;right:10px;bottom:9px;color:rgba(255,255,255,.85);font-size:13.5px}

.catnav{position:absolute;left:10px;top:333px;width:213px;list-style:none;box-shadow:0 2px 6px rgba(60,30,100,.2)}
.catnav li{height:39.5px;line-height:39.5px;padding-left:13px;color:var(--white);font-size:16px;
  background:var(--side-item);border-top:1px solid var(--side-line)}
.catnav li:first-child{border-top:none}
.catnav .is-active{background:var(--side-active);color:var(--heading);font-weight:500}

.content{position:absolute;left:223px;top:333px;width:753px;height:600px;background:var(--panel)}
.content h1{position:absolute;left:23px;top:16px;color:var(--heading);font-size:22px;font-weight:500}
.intro{position:absolute;left:23px;top:57px;width:710px;color:var(--body-text);font-size:15px;line-height:19.5px;text-align:justify}
.brands-label{position:absolute;left:23px;top:158px;color:var(--body-text);font-size:15px}
.brands{position:absolute;left:24px;top:186px;width:709px;height:98px;background:var(--white);
  display:flex;justify-content:space-around;align-items:center;list-style:none;box-shadow:0 1px 3px rgba(0,0,0,.12)}
.brands li{color:var(--logo-ink);font-size:15px;font-weight:500;display:flex;align-items:center;gap:6px}
.brands .mark{width:10px;height:10px;background:var(--logo-ink)}

.products{position:absolute;left:24px;top:302px;display:flex;gap:11px;list-style:none}
.product{width:169px;height:257px;background:var(--white);box-shadow:0 1px 3px rgba(0,0,0,.12);text-align:center;position:relative}
.product-brand{padding-top:9px;color:var(--card-label);font-size:16px;font-weight:500}
.product-photo{margin:6px auto 0;width:112px;height:172px;border-radius:22px 22px 14px 14px}
.photo-charcoal{background:linear-gradient(#4a4a4a,#2c2c2c)}
.photo-orange{background:linear-gradient(#ff6a2a,#e34712)}
.photo-blue{background:linear-gradient(#7fc0e4,#3c8fc0)}
.photo-crimson{background:linear-gradient(#555 0%,#b01e3a 40%,#c22443 70%,#444 100%)}
.product-meta{position:absolute;left:0;right:0;bottom:10px;color:var(--card-price);font-size:15px;line-height:20px}
</style>
</head>
<body>
<div class="canvas">
  <header class="topbar">
    <ul class="topbar-links">
      <li>FIND A STORE</li>
      <li>CONTACT US</li>
      <li>Ph.888-555-0142</li>
    </ul>
    <div class="cart-summary">
      <span>There are XXX items in your cart. $0.00</span>
      <span class="checkout-btn">CHECKOUT</span>
    </div>
  </header>

  <div class="page"></div>

  <div class="logo">
    <div class="logo-name">TIMBERKEEL</div>
    <div class="logo-sub">OUTFITTERS</div>
  </div>

  <div class="search">serch entire store here...</div>
  <svg class="search-btn" viewBox="0 0 32 32" aria-label="Search">
    <defs><linearGradient id="sb" x1="0" y1="0" x2="0" y2="1"><stop offset="0" stop-color="#6cc6f5"/><stop offset="1" stop-color="#1677c9"/></linearGradient></defs>
    <circle cx="16" cy="16" r="15" fill="url(#sb)"/>
    <circle cx="14" cy="14" r="6" fill="none" stroke="#fff" stroke-width="2.5"/>
    <line x1="18.5" y1="18.5" x2="23" y2="23" stroke="#fff" stroke-width="3" stroke-linecap="round"/>
  </svg>

  <div class="stage">
    <ul class="mainnav">
      <li class="is-active">HOME</li>
      <li>WOMEN</li>
      <li>MENS</li>
      <li>GEAR</li>
      <li>ULTRALIGHT</li>
      <li>INSPIRE</li>
      <li>REVIEWS</li>
      <li>ON SALE</li>
    </ul>

    <div class="hero" role="img" aria-label="Paraglider silhouetted against a blue sky above misty mountain ridges">
      <span class="hero-credit">image source www.photo.example</span>
    </div>

    <ul class="catnav">
      <li>SUNGLASSES&nbsp; 355</li>
      <li class="is-active">BACKPACKS 234</li>
      <li>HYDRATION 56</li>
      <li>TENTS AND TRAPS 89</li>
      <li>SLEEPING BAGS 32</li>
      <li>CAMP KITCHEN 70</li>
      <li>ROPES AND CORDAGE 8</li>
    </ul>

    <main class="content">
      <h1>BACKPACKS</h1>
      <p class="intro">Lorem ipsum dolor sit amet, consectetur adipiscing elit. Vestibulum condimentum, turpis ac feugiat sodales, leo eros adipiscing ipsum, vitae volutpat lectus augue vitae urna. Nulla posuere pulvinar dolor, sit amet tempus purus pellentesque quis. Etiam lobortis dolor in risus ullamcorper non consectetur eros pellentesque.</p>
      <p class="brands-label">Our featured brands:.</p>
      <ul class="brands">
        <li>Ridgeline</li>
        <li><span class="mark"></span>Kesto</li>
        <li>Dunmark</li>
        <li>Harrier</li>
        <li>Pinefold</li>
        <li>Slate Summit</li>
      </ul>
      <ul class="products">
        <li class="product">
          <div class="product-brand">BRAND</div>
          <div class="product-photo photo-charcoal" role="img" aria-label="Charcoal daypack"></div>
          <div class="product-meta">PRICE ...... (CAD)<br>MODEL</div>
        </li>
        <li class="product">
          <div class="product-brand">BRAND</div>
          <div class="product-photo photo-orange" role="img" aria-label="Orange climbing pack"></div>
          <div class="product-meta">PRICE ...... (CAD)<br>MODEL</div>
        </li>
        <li class="product">
          <div class="product-brand">BRAND</div>
          <div class="product-photo photo-blue" role="img" aria-label="Light blue alpine pack"></div>
          <div class="product-meta">PRICE ...... (CAD)<br>MODEL</div>
        </li>
        <li class="product">
          <div class="product-brand">BRAND</div>
          <div class="product-photo photo-crimson" role="img" aria-label="Grey and red sling bag"></div>
          <div class="product-meta">PRICE ...... (CAD)<br>MODEL</div>
        </li>
      </ul>
    </main>
  </div>
</div>
</body>
</html>
```